Classic Minimalistic Business Card

Design a classic, minimalistic Business Card. Please find inspiration in the attached Classic Minimalistic examples. My information:
Name: Glen Ovamir
Company: Ovamir Capital
Logo: OC
Address: 1470 N Thornwick Rd, Suite 210 | Brennford, ZZ 00000
Phone: 630-555-0192
Email: glenovamir@pvt.insure
Slogan: Building Strength Through Capital

Feel free to leave out any of the information above except my name.

I have selected Double-sided, but I am also open to Single-sided

Target Market(s)

22-70. income greater than 150k/year

Industry/Entity Type

Finance

Contact Information for Business Card

See Project Description

Requirements
Must have
• Ivory or "antiqued" background similar to the reference pictures

```html
<!DOCTYPE html>
<html lang="en">
<head>
<meta charset="utf-8">
<title>Ovamir Capital – Business Card</title>
<link href="https://fonts.googleapis.com/css2?family=Allura&family=Poppins:wght@400;500;600&display=swap" rel="stylesheet">
<style>
  :root {
    --backdrop: #c4c4c4;
    --card-ivory: #f6f4ee;
    --card-edge: #e6e2d8;
    --ink: #3d3c42;
    --ink-soft: #55545a;
  }
  * { margin: 0; padding: 0; box-sizing: border-box; }
  html, body {
    width: 1200px; height: 900px; overflow: hidden;
    background: var(--backdrop);
  }
  .stage {
    width: 1200px; height: 900px;
    display: flex; flex-direction: column;
    align-items: center; justify-content: center; gap: 34px;
  }
  .card {
    position: relative;
    width: 720px; height: 411px;
    background: linear-gradient(135deg, #fbfaf6 0%, var(--card-ivory) 55%, #efece4 100%);
    border: 1px solid var(--card-edge);
    border-radius: 30px;
    color: var(--ink);
    overflow: hidden;
  }
  .monogram {
    font-family: "Poppins", sans-serif;
    font-weight: 500;
    color: var(--ink);
    letter-spacing: 2px;
    line-height: 1;
  }
  .script {
    font-family: "Allura", cursive;
    color: var(--ink-soft);
    line-height: 1;
  }

  /* Front */
  .card-front .brand-block {
    position: absolute; left: 0; right: 0; top: 92px;
    text-align: center;
  }
  .card-front .monogram { font-size: 92px; }
  .card-front .company-script { font-size: 58px; margin-top: 18px; }
  .card-front .tagline {
    font-family: "Poppins", sans-serif; font-weight: 500;
    font-size: 15px; letter-spacing: 2.2px; text-transform: uppercase;
    margin-top: 14px; color: var(--ink);
  }

  /* Back */
  .card-back .brand-row {
    position: absolute; left: 58px; top: 62px;
    display: flex; align-items: flex-end; gap: 20px;
  }
  .card-back .monogram { font-size: 84px; }
  .card-back .company-script { font-size: 52px; padding-bottom: 10px; }
  .card-back .person-name {
    position: absolute; left: 62px; top: 212px;
    font-size: 54px;
  }
  .card-back .contact-list {
    position: absolute; left: 62px; bottom: 52px;
    list-style: none;
    font-family: "Poppins", sans-serif; font-size: 19px;
    color: var(--ink-soft); line-height: 1.45;
  }
  .card-back .address-block {
    position: absolute; right: 56px; top: 206px;
    text-align: right;
    font-family: "Poppins", sans-serif; font-size: 18px;
    color: var(--ink-soft); line-height: 1.45; font-style: normal;
  }
  .card-back .address-block .address-title {
    font-weight: 600; letter-spacing: 1.5px; text-transform: uppercase;
    color: var(--ink);
  }
</style>
</head>
<body>
  <main class="stage">
    <section class="card card-front" aria-label="Card front">
      <div class="brand-block">
        <div class="monogram">OC</div>
        <div class="script company-script">Ovamir Capital</div>
        <div class="tagline">Building Strength Through Capital</div>
      </div>
    </section>

    <section class="card card-back" aria-label="Card back">
      <div class="brand-row">
        <div class="monogram">OC</div>
        <div class="script company-script">Ovamir Capital</div>
      </div>
      <div class="script person-name">Glen Ovamir</div>
      <ul class="contact-list">
        <li>P: 630-555-0192</li>
        <li>E: glenovamir@pvt.insure</li>
      </ul>
      <address class="address-block">
        <div class="address-title">Ovamir Capital</div>
        <div>1470 N Thornwick Rd</div>
        <div>Suite 210 | Brennford, ZZ 00000</div>
      </address>
    </section>
  </main>
</body>
</html>
```